Creating the Look and Feel of an Elite Boutique Consulting Practice: Vane Advisory

Complete a professional website on Weebly. As part of the site, we are open to a new logo -- we have just launched. We put up a starter website that shows you the content and theme we are going for. But clearly we aren't professional web designers and we need your help. Check out our start at vaneadvisory.com

Target Market(s)

Fortune 500 Clients

Industry/Entity Type

Management Consulting

Logo Text

VANE Advisory

Number of Pages Required

4 page

Requirements
Must have
• I've already set us up on Weebly. I'd like to give the selected designer the log-in credentials and have the designer create it on Weebly, so we can maintain it through that service.

```html
<!DOCTYPE html>
<html lang="en">
<head>
<meta charset="utf-8">
<title>Vane Advisory</title>
<link rel="stylesheet" href="https://fonts.googleapis.com/css2?family=Arimo:ital,wght@0,400;0,700;1,400;1,700&family=Open+Sans:wght@400&display=swap">
<style>
  :root {
    --header-dark: #061214;
    --header-teal: #17343a;
    --page-bg: #ffffff;
    --text: #4a4a4a;
    --title: #2a2a2a;
    --link: #9a9a9a;
    --nav-text: #ffffff;
    --footer: #1c1c1c;
  }
  * { margin: 0; padding: 0; box-sizing: border-box; }
  html, body { width: 1200px; height: 842px; overflow: hidden; }
  body {
    position: relative;
    background: var(--page-bg);
    font-family: "Arimo", Arial, sans-serif;
    color: var(--text);
  }
  .site-header {
    position: absolute; left: 0; top: 0; width: 1200px; height: 133px;
  }
  .header-backdrop {
    position: absolute; inset: 0;
    background: linear-gradient(100deg, var(--header-dark) 0%, #0b1d20 45%, var(--header-teal) 80%, #0e2226 100%);
  }
  .brand {
    position: absolute; left: 142px; top: 27px;
    font-family: "Open Sans", Arial, sans-serif;
    font-size: 22px; color: var(--nav-text); letter-spacing: 0.2px;
  }
  .main-nav {
    position: absolute; top: 22px; left: 671px;
    display: flex; gap: 0;
    font-family: "Open Sans", Arial, sans-serif;
    font-size: 13.5px; color: var(--nav-text);
  }
  .main-nav a {
    color: inherit; text-decoration: none;
    height: 36px; line-height: 34px; padding: 0 13px;
    border: 1.5px solid transparent; border-radius: 3px;
    margin-right: 15px;
  }
  .main-nav a.current { border-color: var(--nav-text); }
  .page-title {
    position: absolute; left: 0; width: 1185px; top: 224px;
    text-align: center; font-size: 51px; font-weight: 400;
    color: var(--title); letter-spacing: 0.5px;
  }
  .page-title strong { font-weight: 700; }
  .section-heading {
    position: absolute; left: 142px;
    font-size: 15px; font-weight: 700;
  }
  .point-list {
    position: absolute; left: 187px; width: 870px;
    font-size: 13.2px; line-height: 19.7px;
  }
  .point-list li { margin-bottom: 3px; }
  .point-list li::marker { font-size: 11px; }
  .point-list em { font-weight: 700; }
  .point-list a { color: var(--link); }
  .team-list li.ready { margin-top: 5px; }
  .site-footer {
    position: absolute; left: 0; top: 831px; width: 1200px; height: 11px;
    background: var(--footer);
  }
</style>
</head>
<body>
  <header class="site-header">
    <div class="header-backdrop" role="img" aria-label="Dark teal photograph of a city structure behind the navigation bar"></div>
    <div class="brand">VANE ADVISORY</div>
    <nav class="main-nav">
      <a class="current" href="#">HOME</a>
      <a href="#">TEAM</a>
      <a href="#">CONTACT</a>
      <a href="#">APPROACH</a>
    </nav>
  </header>

  <h1 class="page-title"><strong>VANE</strong> ADVISORY</h1>

  <h2 class="section-heading" style="top:320px">We help your organization achieve a successful, resilient transformation by:</h2>
  <ul class="point-list" style="top:348px">
    <li>Partnering with you to clarify and communicate your transformational purpose.<br><em>Where are you going? What will you become?<br>Why change now?</em></li>
    <li>Assessing the current state of your organization.<br><em>Where are you today? What should be protected and preserved? What needs to change?</em></li>
    <li>Building innovative engagements to help people master the skillets and mindsets needed for your current and future context.<br><em>What programs and projects should be created to ensure your leaders are ready, willing, able and excited to lead the transformation?</em></li>
    <li>Embedding routines and practices to ensure the transformation is structurally resilient.<br><em>How should future work be divided, done and measured?</em></li>
  </ul>

  <h2 class="section-heading" style="top:556px">The people of VANE ADVISORY&nbsp; are:</h2>
  <ul class="point-list team-list" style="top:607px">
    <li><em>Experienced.</em><br>Over the past three decades, we have deep experience driving organizational transformation in more than 33 countries, for some of the world's largest, most transformative companies in your industry.</li>
    <li><em>Curious.</em><br>Each of the dozens of transformations we've enabled are unique. Our most relevant experience is our ability to listen and learn where you want to go, and to partner with you to create an original set of tools and experiences to help your people get there. If you're curious, learn more about our <a href="#">team</a>.</li>
    <li class="ready"><em>Ready to Hear Your Story.</em><br>Of course the best way to get to know more about us is to <a href="#">contact us</a>, get to know us, and see what you think.</li>
  </ul>

  <footer class="site-footer"></footer>
</body>
</html>
```